Business card for law firm

Need business card for new law firm. Think confident, authoritative, conservative, but not stuffy or old-fashioned.

Contact Information for Business Card

Content for card - logo (uploaded), plus the following:

Paul Weybridge (larger font)
Managing Partner (larger font, but not as large as name)
Level 9, 47 Calder Lane
Sydney NSW 2000
Main Tel 02 7304 6219
Direct Tel 02 7462 3158
Email paul@wbrlegal.com.au
www.wbrlegal.com.au

Letterhead design should include logo plus:
Level 9, 47 Calder Lane
Sydney NSW 2000
Tel 02 7462 3158
www.wbrlegal.com.au

```html
<!DOCTYPE html>
<html lang="en">
<head>
<meta charset="utf-8">
<title>Weybridge Legal — Business Card</title>
<link rel="stylesheet" href="https://fonts.googleapis.com/css2?family=Cinzel:wght@400;500&family=Jost:wght@400&display=swap">
<style>
  :root {
    --navy: #001d56;
    --black: #050505;
    --white: #ffffff;
    --ink: #1a1a1a;
    --contact: #2b3550;
    --address: #6f6f6f;
    --backdrop: #e4e4e4;
  }
  * { margin: 0; padding: 0; box-sizing: border-box; }
  html, body { width: 1125px; height: 1200px; overflow: hidden; }
  body { background: var(--backdrop); position: relative; font-family: "Jost", sans-serif; }

  .card { position: absolute; left: 145px; width: 800px; height: 456px; }
  .card--front { top: 95px; background: var(--white); }
  .card--back { top: 611px; background: var(--navy); }

  .name-band {
    position: absolute; left: 0; top: 46px; width: 548px; height: 98px;
    background: var(--navy); color: var(--white);
    font-family: "Cinzel", serif; padding: 20px 0 0 50px;
  }
  .name-band__name { font-size: 32px; font-weight: 500; letter-spacing: 0.5px; line-height: 1.1; }
  .name-band__title { font-size: 21px; font-weight: 500; letter-spacing: 0.8px; line-height: 1.2; margin-top: 4px; }

  .mark-square { position: absolute; left: 552px; top: 46px; width: 74px; height: 98px; background: var(--navy); }
  .black-block { position: absolute; left: 629px; top: 46px; width: 171px; height: 98px; background: var(--black); }

  .wordmark {
    position: absolute; right: 58px; top: 176px;
    font-family: "Cinzel", serif; font-weight: 400; font-size: 40px;
    color: var(--ink); letter-spacing: 2px; white-space: nowrap;
  }

  .contacts { position: absolute; left: 45px; top: 334px; list-style: none; }
  .contacts li { display: flex; align-items: center; height: 26px; font-size: 21px; color: var(--contact); }
  .contacts svg { width: 20px; height: 20px; margin-right: 15px; fill: var(--navy); }

  .address {
    position: absolute; right: 52px; top: 338px; text-align: right;
    font-size: 21px; line-height: 26px; color: var(--address); font-style: normal;
  }

  .back-wordmark {
    position: absolute; left: 0; right: 0; top: 50%; transform: translateY(-50%);
    text-align: center; font-family: "Cinzel", serif; font-weight: 400;
    font-size: 52px; letter-spacing: 3px; color: var(--white);
  }
</style>
</head>
<body>
  <section class="card card--front">
    <div class="name-band">
      <div class="name-band__name">PAUL WEYBRIDGE</div>
      <div class="name-band__title">MANAGING PARTNER</div>
    </div>
    <div class="mark-square"></div>
    <div class="black-block"></div>

    <div class="wordmark">WEYBRIDGE LEGAL</div>

    <ul class="contacts">
      <li>
        <svg viewBox="0 0 20 20" aria-hidden="true"><path d="M2 7c0-3 4-4 8-4s8 1 8 4v2h-4V7H6v2H2z"/><path d="M5 10h10l2 7H3z"/><circle cx="10" cy="13.5" r="2" fill="#fff"/></svg>
        02 7304 6219
      </li>
      <li>
        <svg viewBox="0 0 20 20" aria-hidden="true"><path d="M6 1h8a1 1 0 0 1 1 1v16a1 1 0 0 1-1 1H6a1 1 0 0 1-1-1V2a1 1 0 0 1 1-1zm1 3v11h6V4z"/></svg>
        02 7462 3158
      </li>
      <li>
        <svg viewBox="0 0 20 20" aria-hidden="true"><path d="M2 6h16v1l-8 5-8-5z"/><path d="M2 9l8 5 8-5v6H2z"/></svg>
        paul@wbrlegal.com.au
      </li>
    </ul>

    <address class="address">
      Level 9, 47 Calder Lane<br>
      Sydney NSW 2000<br>
      www.wbrlegal.com.au
    </address>
  </section>

  <section class="card card--back">
    <div class="back-wordmark">WEYBRIDGE LEGAL</div>
  </section>
</body>
</html>
```